Construction Company

Design a clutter free business card, it can be double-sided utilizing the logo for BDN Ltd simple with all relevant contact information.

Please also a letterhead design to function for the purposes of invoicing, all mail requirements, with header to be distinctive while the footer ties page together and incorporates all necessary information.

For now, please use generic / dummy text and when a winner is selected, I will disclose the contact information.

Hi Designers! Please read the updated brief which includes the design of a business card and letterhead. Thank you!

```html
<!DOCTYPE html>
<html lang="en">
<head>
<meta charset="UTF-8">
<title>BDN Ltd – Business Card</title>
<link rel="stylesheet" href="https://fonts.googleapis.com/css2?family=Open+Sans:wght@400;600;800&display=swap">
<style>
  :root {
    --navy: #283c8c;
    --gold: #b08d3a;
    --ink: #4a4a4a;
    --paper: #ffffff;
    --backdrop: #e9e9ec;
  }
  * { margin: 0; padding: 0; box-sizing: border-box; }
  html, body {
    width: 1200px;
    height: 900px;
    overflow: hidden;
    background: var(--backdrop);
    font-family: "Open Sans", Arial, sans-serif;
  }
  .sheet {
    position: relative;
    width: 1200px;
    height: 900px;
  }
  .card {
    position: absolute;
    left: 265px;
    width: 670px;
    height: 383px;
    box-shadow: 0 6px 18px rgba(0,0,0,0.18);
  }
  .card--front { top: 42px; background: var(--navy); }
  .card--back  { top: 470px; background: var(--paper); }

  .brand {
    position: absolute;
    display: flex;
    align-items: center;
    gap: 14px;
    font-weight: 600;
    letter-spacing: 1px;
    white-space: nowrap;
  }
  .brand__dot {
    border-radius: 50%;
    background: var(--gold);
    flex: none;
  }
  .card--front .brand {
    left: 50%;
    top: 50%;
    transform: translate(-50%, -50%);
    font-size: 64px;
    color: var(--paper);
  }
  .card--front .brand__dot { width: 34px; height: 34px; }

  .card--back .brand {
    left: 48px;
    top: 56px;
    font-size: 44px;
    color: var(--navy);
  }
  .card--back .brand__dot { width: 24px; height: 24px; }

  .holder {
    position: absolute;
    right: 36px;
    top: 48px;
    text-align: right;
  }
  .holder__name {
    font-weight: 800;
    font-size: 24px;
    color: var(--navy);
    letter-spacing: 0.3px;
  }
  .holder__role {
    font-size: 15px;
    color: var(--ink);
    margin-top: 2px;
  }

  .divider {
    position: absolute;
    left: 150px;
    right: 28px;
    top: 214px;
    height: 1.5px;
    background: var(--navy);
  }

  .contact {
    position: absolute;
    left: 150px;
    top: 232px;
    list-style: none;
    font-size: 17px;
    color: var(--ink);
    line-height: 1.5;
  }
  .contact__item { display: flex; align-items: center; gap: 8px; }
  .contact__icon { width: 14px; height: 14px; flex: none; }

  .address {
    position: absolute;
    right: 36px;
    top: 232px;
    text-align: right;
    font-size: 17px;
    color: var(--ink);
    line-height: 1.5;
    font-style: normal;
  }
</style>
</head>
<body>
<main class="sheet">

  <section class="card card--front" aria-label="Business card front">
    <div class="brand">
      <span class="brand__dot"></span>
      <span class="brand__name">BDN Ltd</span>
    </div>
  </section>

  <section class="card card--back" aria-label="Business card back">
    <div class="brand">
      <span class="brand__dot"></span>
      <span class="brand__name">BDN Ltd</span>
    </div>

    <div class="holder">
      <p class="holder__name">DANIEL WHITCOMB</p>
      <p class="holder__role">President</p>
    </div>

    <div class="divider"></div>

    <ul class="contact">
      <li class="contact__item">
        <svg class="contact__icon" viewBox="0 0 16 16" aria-hidden="true">
          <circle cx="8" cy="8" r="8" fill="var(--gold)"/>
          <path d="M5 4.2c.4-.3.9-.2 1.1.2l.8 1.5c.2.4.1.8-.2 1l-.5.4c.5 1 1.2 1.7 2.2 2.2l.4-.5c.3-.3.7-.4 1-.2l1.5.8c.4.2.5.7.2 1.1l-.6.7c-.4.4-1 .5-1.6.3C7.3 10.9 5.1 8.7 4.3 6.6c-.2-.6-.1-1.2.3-1.6z" fill="#fff"/>
        </svg>
        555-240-0187
      </li>
      <li class="contact__item">
        <svg class="contact__icon" viewBox="0 0 16 16" aria-hidden="true">
          <rect x="0" y="2.5" width="16" height="11" rx="1.5" fill="var(--gold)"/>
          <path d="M1.5 4l6.5 5 6.5-5" fill="none" stroke="#fff" stroke-width="1.3"/>
        </svg>
        dwhitcomb@bdnltd.com
      </li>
      <li class="contact__item">
        <svg class="contact__icon" viewBox="0 0 16 16" aria-hidden="true">
          <circle cx="8" cy="8" r="8" fill="var(--gold)"/>
          <circle cx="8" cy="8" r="5" fill="none" stroke="#fff" stroke-width="1"/>
          <ellipse cx="8" cy="8" rx="2.2" ry="5" fill="none" stroke="#fff" stroke-width="1"/>
          <path d="M3 8h10" stroke="#fff" stroke-width="1"/>
        </svg>
        www.bdnltd.com
      </li>
    </ul>

    <address class="address">
      1820 Harbor View Drive<br>
      Seaview CA 90000
    </address>
  </section>

</main>
</body>
</html>
```